Saffron Ledger Works Flyer

We need a one page promotional piece that explains what our company does, and the benefits it provides in a simple, elegant, easy to understand way. I would like to print it on glossy heavyweight paper to give a feel of high quality and legitimacy. I will include the logo, the tag line, and the main benefits that the company offers.

Tag line concept, may not need these exact words. "Give us 5 minutes a day, and we will help you build a Saffron Ledger Works."

Key points...(exact wording not required if you think of a better way to say it)

Software easy enough for my grandpa to use.
Lets you use snail mail, email, texting, and social media to quickly market to your customers at very low cost.
Web based which allows you to launch media campaigns from your desktop, or smartphone in moments.
Quick 3 - 5 minute training videos which give you hard hitting, quick action tips that will help you make your business better today.
Live coaching calls to help motivate you to improve your business.
No contracts, or start up fees. One low price of $299 per month.

Restaurant owners

Restaurant

```html
<!DOCTYPE html>
<html lang="en">
<head>
<meta charset="utf-8">
<title>Saffron Ledger Works Flyer</title>
<link rel="stylesheet" href="https://fonts.googleapis.com/css2?family=PT+Sans+Narrow:wght@400;700&display=swap">
<style>
  :root {
    --paper-top: #f4f5f5;
    --paper-mid: #dfe3e2;
    --band-white: #ffffff;
    --teal-light: #7b9894;
    --teal-mid: #3f6661;
    --teal-deep: #0e3732;
    --ink-dark: #2e2e2e;
    --ink-grey: #5a5a5a;
    --text-white: #ffffff;
    --accent-gold: #f3c229;
    --stamp-shadow: rgba(0, 0, 0, 0.35);
  }
  * { margin: 0; padding: 0; box-sizing: border-box; }
  html, body { width: 849px; height: 1200px; overflow: hidden; background: var(--paper-top); }
  .flyer {
    position: relative;
    width: 849px;
    height: 1200px;
    overflow: hidden;
    font-family: "PT Sans Narrow", "Arial Narrow", sans-serif;
  }
  .header {
    position: absolute;
    left: 0; top: 0;
    width: 849px; height: 400px;
    background: linear-gradient(180deg, var(--paper-top) 0%, var(--paper-mid) 100%);
  }
  .header-art {
    position: absolute;
    inset: 0;
    background: radial-gradient(ellipse 420px 300px at 50% 55%, rgba(255,255,255,0.6), rgba(200,206,205,0.25) 70%, transparent 100%);
  }
  .brand {
    position: absolute;
    left: 0; top: 290px;
    width: 849px;
    display: flex;
    align-items: center;
    justify-content: center;
    gap: 16px;
  }
  .brand-dot {
    width: 34px; height: 34px;
    border-radius: 50%;
    background: var(--ink-grey);
  }
  .brand-name {
    font-weight: 700;
    font-size: 46px;
    color: var(--ink-grey);
    letter-spacing: 1px;
  }
  .tagline-band {
    position: absolute;
    left: 0; top: 400px;
    width: 849px; height: 96px;
    background: var(--band-white);
    display: flex;
    align-items: center;
    justify-content: center;
  }
  .tagline {
    text-align: center;
    font-size: 28px;
    line-height: 36px;
    color: var(--ink-dark);
  }
  .tagline strong { font-weight: 700; }
  .benefits-panel {
    position: absolute;
    left: 0; top: 496px;
    width: 849px; height: 704px;
    background: linear-gradient(180deg, var(--teal-light) 0%, var(--teal-mid) 45%, var(--teal-deep) 100%);
  }
  .benefit-list {
    list-style: none;
    position: absolute;
    left: 127px; top: 26px;
    width: 640px;
    color: var(--text-white);
    font-size: 28px;
    line-height: 38px;
  }
  .benefit-list li { margin-bottom: 20px; }
  .benefit-list b { font-weight: 700; }
  .highlight { color: var(--accent-gold); }
  .price-stamp {
    position: absolute;
    left: 343px; top: 988px;
    width: 390px;
    padding: 14px 10px 12px;
    background: var(--band-white);
    color: var(--ink-dark);
    text-align: center;
    font-size: 28px;
    line-height: 34px;
    transform: rotate(-6deg);
    box-shadow: 2px 4px 10px var(--stamp-shadow);
  }
  .price-stamp b { font-weight: 700; }
</style>
</head>
<body>
<main class="flyer">
  <header class="header">
    <div class="header-art" role="img" aria-label="Faint oversized fork and knife decoration behind the logo"></div>
    <div class="brand">
      <span class="brand-dot"></span>
      <span class="brand-name">Saffron Ledger Works</span>
    </div>
  </header>

  <section class="tagline-band">
    <p class="tagline">Give us 5 minutes a day and we will give you 5 reasons<br>and our help to build a <strong>Saffron Ledger Works</strong>.</p>
  </section>

  <section class="benefits-panel">
    <ol class="benefit-list">
      <li>1. Software <span class="highlight">easy</span> enough <b>for my grandpa to use.</b></li>
      <li>2. Lets you use snail mail, email, texting, and social media<br><b>to quickly market to your customers at <span class="highlight">very low cost</span>.</b></li>
      <li>3. Web based so you can launch media campaigns<br><b><span class="highlight">from your desktop or smartphone,</span> in moments.</b></li>
      <li>4. Quick 3 - 5 minute training videos which give you<br><b>hard hitting, quick action tips that will help you<br><span class="highlight">make your business better today</span>.</b></li>
      <li>5. Live coaching calls to <b>help motivate you<br>to <span class="highlight">improve your business</span>.</b></li>
    </ol>
  </section>

  <aside class="price-stamp">
    No contracts or start up fees.<br>
    <b>One low price of $299 per month.</b>
  </aside>
</main>
</body>
</html>
```